Baseball field Banner

approx 5x7 ft banner on baseball field fence on busy street. Need high visibility colors for traffic passing by. Emphasis on Velmo Orthodontics and Braces $1999. The uploaded sample is only an example, but all the content needs to be included in design.

```html
<!DOCTYPE html>
<html lang="en">
<head>
<meta charset="utf-8">
<title>Velmo Orthodontics – Baseball Field Banner</title>
<link rel="stylesheet" href="https://fonts.googleapis.com/css2?family=Oswald:wght@300;400;600;700&display=swap">
<style>
  :root {
    --black: #000000;
    --gold: #f2a51a;
    --gold-light: #ffd23a;
    --gold-deep: #d9821a;
    --white: #f4f4f4;
    --field-dark: #1c2a15;
    --field: #33451f;
    --dirt: #3a2218;
    --crowd: #1a1412;
  }
  * { margin: 0; padding: 0; box-sizing: border-box; }
  html, body { width: 1200px; height: 1200px; overflow: hidden; background: var(--black); }
  .banner { position: relative; width: 1200px; height: 1200px; background: var(--black); font-family: "Oswald", sans-serif; color: var(--white); }
  .field-photo {
    position: absolute; left: 0; top: 172px; width: 1200px; height: 856px;
    background:
      radial-gradient(ellipse 55% 30% at 50% 62%, rgba(70,40,28,0.75), transparent 70%),
      linear-gradient(180deg, var(--crowd) 0%, #2a2320 12%, var(--field-dark) 18%, var(--field) 45%, var(--field-dark) 70%, var(--dirt) 85%, var(--crowd) 100%);
  }
  .abs { position: absolute; }
  .center { transform: translateX(-50%); text-align: center; white-space: nowrap; }
  .headline {
    left: 598px; top: 196px; font-weight: 600; font-size: 66px; letter-spacing: 11px; line-height: 1;
    background: linear-gradient(180deg, var(--gold-light), var(--gold-deep));
    -webkit-background-clip: text; background-clip: text; color: transparent;
  }
  .brand { left: 352px; top: 290px; display: flex; align-items: center; gap: 24px; }
  .brand-mark { width: 144px; height: 144px; border-radius: 50%; border: 11px solid var(--gold); }
  .brand-name { color: var(--gold); font-weight: 400; line-height: 0.95; }
  .brand-name .line1 { display: block; font-size: 96px; letter-spacing: 3px; }
  .brand-name .line2 { display: block; font-size: 50px; letter-spacing: 4px; }
  .feature { font-weight: 300; font-size: 26px; letter-spacing: 5px; line-height: 1.3; }
  .price {
    left: 578px; top: 570px; font-weight: 600; font-size: 76px; letter-spacing: 9px; line-height: 1;
    background: linear-gradient(180deg, var(--gold-light), var(--gold-deep));
    -webkit-background-clip: text; background-clip: text; color: transparent;
  }
  .monthly { left: 578px; top: 692px; color: var(--gold); font-weight: 600; font-size: 34px; letter-spacing: 5px; }
  .support { left: 36px; top: 858px; font-weight: 300; font-size: 32px; letter-spacing: 6px; line-height: 1.4; }
  .contact { top: 950px; color: var(--gold); font-weight: 600; font-size: 42px; letter-spacing: 4px; line-height: 1; }
  .web { left: 36px; }
  .phone { right: 36px; letter-spacing: 4px; }
  .corner-brand { left: 960px; top: 836px; display: flex; align-items: center; gap: 10px; }
  .corner-mark { width: 84px; height: 84px; border-radius: 50%; border: 8px solid var(--gold); }
  .corner-name { color: var(--gold); font-size: 26px; font-weight: 400; letter-spacing: 2px; }
  .icon { stroke: var(--white); fill: none; stroke-width: 3; }
</style>
</head>
<body>
<main class="banner">
  <div class="field-photo" role="img" aria-label="Evening view of a baseball stadium infield with players on the field and crowded stands"></div>

  <h1 class="abs center headline">HIT A HOMERUN WITH:</h1>

  <div class="abs brand">
    <div class="brand-mark"></div>
    <div class="brand-name"><span class="line1">VELMO</span><span class="line2">ORTHODONTICS</span></div>
  </div>

  <svg class="abs icon" style="left:560px;top:472px" width="48" height="40" viewBox="0 0 48 40" aria-hidden="true">
    <rect x="2" y="2" width="44" height="36" rx="2"/>
    <rect x="8" y="8" width="32" height="24"/>
    <path d="M18 14c3-2 5 0 6 0s3-2 6 0c2 2 0 6-1 10h-3l-2-4-2 4h-3c-1-4-3-8-1-10z"/>
  </svg>
  <p class="abs center feature" style="left:590px;top:522px">X-RAYS INCLUDED</p>

  <p class="abs center price">BRACES $1999</p>
  <p class="abs center feature" style="left:575px;top:656px">STARTING FROM</p>
  <p class="abs center monthly">$87/MO</p>

  <svg class="abs icon" style="left:152px;top:588px" width="50" height="50" viewBox="0 0 50 50" aria-hidden="true">
    <circle cx="18" cy="14" r="10"/>
    <path d="M2 46c0-12 7-18 16-18s12 4 13 8"/>
    <path d="M30 34c3-3 6-1 8-1s5-2 8 1c2 3-1 8-2 12h-3l-3-5-3 5h-3c-1-4-4-9-2-12z"/>
  </svg>
  <p class="abs center feature" style="left:176px;top:654px">ALL<br>APPOINTMENTS<br>INCLUDED</p>

  <svg class="abs" style="left:970px;top:584px" width="54" height="54" viewBox="0 0 54 54" aria-hidden="true">
    <circle cx="27" cy="27" r="23" stroke="var(--white)" stroke-width="5" fill="none"/>
    <path d="M35 18c-2-3-14-4-14 3s14 4 14 12-13 6-15 2M27 10v34" stroke="var(--white)" stroke-width="4" fill="none"/>
    <path d="M11 11l32 32" stroke="var(--white)" stroke-width="5"/>
  </svg>
  <p class="abs center feature" style="left:999px;top:656px">FREE<br>CONSULTATION</p>

  <p class="abs center feature" style="left:586px;top:756px">RETAINERS INCLUDED!</p>
  <svg class="abs" style="left:552px;top:800px" width="52" height="56" viewBox="0 0 52 56" aria-hidden="true">
    <path d="M26 14c-4-10-16-10-12-2 2 3 8 2 12 2zm0 0c4-10 16-10 12-2-2 3-8 2-12 2z" stroke="var(--white)" stroke-width="3" fill="none"/>
    <rect x="2" y="16" width="48" height="12" fill="var(--white)"/>
    <rect x="6" y="31" width="40" height="24" fill="var(--white)"/>
    <rect x="23" y="16" width="6" height="40" fill="var(--field)"/>
  </svg>

  <p class="abs support">PROUDLY SUPPORTING<br>PINE HOLLOW YOUTH BALL</p>

  <div class="abs corner-brand">
    <div class="corner-mark"></div>
    <span class="corner-name">VELMO</span>
  </div>

  <p class="abs contact web">VELMOORTHODONTICS.COM</p>
  <p class="abs contact phone">310-555-0142</p>
</main>
</body>
</html>
```